WYN Football Academy Flyer

Flyer for a full page of a yearbook ( dimensions below ) along with all the contents/photos for the flyer.
Width - 210 mm
Height - 297 mm
Please also see attached the previous flyer which we feel is in need of an upgrade !
Flyer will also be used on social media pages.
Creating next level athletes !
Providing a platform and the correct environment for young football players to develop and fulfil their potential.
Why choose WYN Football Academy
- Multiple programs for everyone
- KAVO qualified & experienced coaches
- Safe and fun environment
- All coaches police checked
- Coaches Emergency First Aid Qualified
- Coaches Safeguarding Children Qualified
- Develop new skills
- Make new friends
- Improve your fitness
REGISTER NOW!
www.tidelumenworks.com
+968 412 30967
Instagram/Facebook - wynfootballacademy

```html
<!DOCTYPE html>
<html lang="en">
<head>
<meta charset="utf-8">
<title>WYN Football Academy Flyer</title>
<link href="https://fonts.googleapis.com/css2?family=Bebas+Neue&family=Urbanist:wght@400;500;700;800&display=swap" rel="stylesheet">
<style>
:root{
  --green:#6dbd45;
  --green-dark:#4f9a2f;
  --ink:#1d1d1d;
  --text:#2e2e2e;
  --panel:#e9ebed;
  --paper:#ffffff;
  --backdrop:#d3d3d3;
  --night:#0d2236;
  --sky:#2f5f80;
}
*{box-sizing:border-box;margin:0;padding:0}
html,body{width:1200px;height:2400px;overflow:hidden}
body{background:var(--backdrop);font-family:"Urbanist",sans-serif;color:var(--text);position:relative}
.flyer{position:absolute;left:100px;top:493px;width:1000px;height:1414px;background:var(--paper);overflow:hidden;box-shadow:0 30px 50px rgba(0,0,0,.25)}
.brand{position:absolute;left:58px;top:90px;width:160px;color:var(--green);font-weight:800;line-height:1.05}
.brand-dot{width:46px;height:46px;border-radius:50%;background:var(--green);margin-bottom:14px}
.brand-name{font-size:34px}
.brand-sub{font-size:22px}
.accent-bar{position:absolute;left:274px;top:0;width:15px;height:365px;background:var(--green)}
.hero{position:absolute;left:0;top:0;width:1000px;height:820px}
.headline{position:absolute;left:0;top:0;width:1000px;height:820px;font-family:"Bebas Neue",sans-serif}
.intro{position:absolute;left:58px;top:782px;width:560px;font-size:29px;line-height:46px;color:var(--text);font-weight:400}
.intro strong{color:var(--green);font-weight:700}
.snap{position:absolute;background:var(--paper);padding:8px 8px 22px;box-shadow:0 6px 14px rgba(0,0,0,.3)}
.snap .shot{width:100%;height:100%;background:linear-gradient(160deg,#dfe6e2 0%,#3f8d4a 55%,#2a6b33 100%)}
.snap .tag{position:absolute;right:14px;bottom:5px;font-size:9px;color:#555}
.panel{position:absolute;left:372px;top:987px;width:628px;height:262px;background:var(--panel);border-top:3px solid var(--green);border-bottom:3px solid var(--green)}
.panel-title{position:absolute;left:0;width:628px;top:30px;text-align:center;font-size:29px;font-weight:700;color:#333}
.reasons{position:absolute;top:76px;list-style:none;font-size:18px;line-height:26px;color:#3a3a3a}
.reasons li{padding-left:20px;position:relative}
.reasons li::before{content:"";position:absolute;left:2px;top:7px;width:6px;height:10px;border-right:2.5px solid var(--green);border-bottom:2.5px solid var(--green);transform:rotate(40deg)}
.reasons.col-a{left:20px}
.reasons.col-b{left:364px}
.reasons .cont{padding-left:20px}
.reasons .cont::before{display:none}
.register{position:absolute;left:510px;top:1216px;width:312px;height:63px;border-radius:14px;background:var(--green);color:#fff;font-family:"Bebas Neue",sans-serif;font-size:44px;line-height:66px;text-align:center;letter-spacing:1px}
.footer{position:absolute;left:0;top:1300px;width:1000px;height:70px}
.social{position:absolute;left:50px;top:0;width:150px;text-align:center;font-size:13px;color:#333}
.social-dot{width:24px;height:24px;border-radius:50%;background:var(--green);margin:0 auto 6px}
.contact{position:absolute;top:8px;display:flex;align-items:center;gap:14px;font-size:26px;font-weight:500;color:#222}
.contact.phone{left:236px}
.contact.web{left:520px}
.base-band{position:absolute;left:0;bottom:0;width:1000px;height:28px;background:var(--green)}
</style>
</head>
<body>
<div class="flyer">

  <svg class="hero" viewBox="0 0 1000 820" role="img" aria-label="Young footballer in green kit controlling a ball in a floodlit stadium at dusk">
    <defs>
      <linearGradient id="stadium" x1="0" y1="0" x2="0" y2="1">
        <stop offset="0" stop-color="#0b1c2e"/>
        <stop offset=".45" stop-color="#2d5b7c"/>
        <stop offset=".72" stop-color="#163247"/>
        <stop offset=".85" stop-color="#3f8c3a"/>
        <stop offset="1" stop-color="#2d6d2b"/>
      </linearGradient>
    </defs>
    <path d="M306,0 H1000 V560 L900,770 H600 L560,710 L530,560 L460,470 L390,470 L380,370 H306 Z" fill="url(#stadium)"/>
    <path d="M1000,560 L900,770 H600" fill="none" stroke="var(--green)" stroke-width="10"/>
  </svg>

  <div class="accent-bar"></div>

  <div class="brand">
    <div class="brand-dot"></div>
    <div class="brand-name">WYN</div>
    <div class="brand-sub">Football Academy</div>
  </div>

  <svg class="headline" viewBox="0 0 1000 820" aria-label="Creating next level athletes">
    <text x="58" y="452" font-size="104" fill="var(--ink)" font-family="Bebas Neue, sans-serif">CREATING</text>
    <text x="52" y="598" font-size="178" fill="var(--green)" font-family="Bebas Neue, sans-serif" letter-spacing="-2">NEXT</text>
    <text x="330" y="598" font-size="94" fill="var(--ink)" font-family="Bebas Neue, sans-serif">LEVEL</text>
    <text x="52" y="739" font-size="178" fill="var(--green)" font-family="Bebas Neue, sans-serif" letter-spacing="-2">ATHLETES</text>
  </svg>

  <p class="intro">Providing a platform and the correct environment for <strong>young football</strong> players to develop and <strong>fulfil their potential</strong></p>

  <div class="snap" style="left:712px;top:630px;width:128px;height:190px;transform:rotate(3deg)"><div class="shot" role="img" aria-label="Young players training indoors"></div></div>
  <div class="snap" style="left:835px;top:580px;width:170px;height:200px;transform:rotate(6deg)"><div class="shot" role="img" aria-label="Players contesting the ball on a pitch"></div></div>
  <div class="snap" style="left:598px;top:795px;width:162px;height:185px;transform:rotate(-3deg)"><div class="shot" role="img" aria-label="Team holding a trophy"></div></div>
  <div class="snap" style="left:780px;top:785px;width:225px;height:210px;transform:rotate(4deg)"><div class="shot" role="img" aria-label="Squad with medals posing together"></div><span class="tag">@wynfootballacademy</span></div>
  <div class="snap" style="left:8px;top:935px;width:360px;height:290px;transform:rotate(-3deg)"><div class="shot" role="img" aria-label="Girls team group photo on the pitch"></div></div>

  <div class="panel">
    <h2 class="panel-title">Why choose WYN Football Academy :</h2>
    <ul class="reasons col-a">
      <li>Multiple programs for everyone</li>
      <li>KAVO qualified &amp; experienced coaches</li>
      <li>Safe and fun environment</li>
      <li>All coaches police checked</li>
      <li>Coaches Emergency First Aid Qualified</li>
    </ul>
    <ul class="reasons col-b">
      <li>Coaches Safeguarding</li>
      <li class="cont">Children Qualified</li>
      <li>Develop new skills</li>
      <li>Make new friends</li>
      <li>Improve your fitness</li>
    </ul>
  </div>

  <div class="register">REGISTER NOW</div>

  <div class="footer">
    <div class="social"><div class="social-dot"></div>wynfootballacademy</div>
    <div class="contact phone">
      <svg width="34" height="34" viewBox="0 0 34 34" aria-hidden="true"><circle cx="17" cy="17" r="15" fill="none" stroke="var(--green)" stroke-width="2.5"/><path d="M11 10c1-1 2-1 3 0l2 3c.6 1 .3 1.8-.5 2.4-.8.6-.6 1.4.3 2.6s1.8 1.7 2.6.9c.7-.7 1.5-.9 2.4-.3l2.6 1.8c1 .8 1 1.8 0 2.8-2 2-5 1.4-8.6-2.2S9 12 11 10z" fill="var(--green)"/></svg>
      <span>+968 412 30967</span>
    </div>
    <div class="contact web">
      <svg width="36" height="36" viewBox="0 0 36 36" aria-hidden="true" fill="none" stroke="var(--green)" stroke-width="2.2"><circle cx="18" cy="18" r="15"/><ellipse cx="18" cy="18" rx="7" ry="15"/><path d="M3 18h30M5.5 10h25M5.5 26h25"/></svg>
      <span>www.tidelumenworks.com</span>
    </div>
  </div>

  <div class="base-band"></div>
</div>
</body>
</html>
```